Bakery Needs Packaging Design for Gourmet Sandwich Cookie

Packaging design will be for sandwich cookies to be wrapped individually for sale. Our product is a premium sandwich cookie, with a dulce-de-leche (caramel-colored) filling. The cookie is topped with a white coating of powdered sugar. Dessert has Peruvian origin, however do not want to explicitly use red and white (Peruvian flag colors). The design should evoke the luxurious nature of our dessert and complement well with our product's' colors. Would like to see a gold/caramel color predominantly. Please see attached for image of product we took (own).
Updates

Reason: Did not give ample time to suggest revisions.

Target Market(s)

As our product is a gourmet product, it should reach those willing to spend a premium for quality and taste.

Industry/Entity Type

Bakery

Font styles to use
Script

Requirements
Must have
• Image of our product (see attachments), either one or two cookies, whichever is best applicable to design.
• Name of our Company = Ventoras (NOT Ramoncho)
• "Gourmet Alfajores" is the name of this particular product
• "est. 1996" somewhere on the label.
Nice to have
• Please see our draft in the attachment. This is simply an inspiration. Please feel free to suggest improvements to this design, or submit a completely new, unique one. We are seeking combinations of colors that pair well and emphasize the elegance of our product.
Should not have
• Although our cookie is a Peruvian cookie, it should not limit itself to red and white colors (Peruvian flag colors).
• "Ramoncho" It is not our company name anymore. It is now "Ventoras" this should be in script.
• "Alfajores Peruanos" - It should simply say "Gourmet Alfajores" should be in print (for visibility)

```html
<!DOCTYPE html>
<html lang="en">
<head>
<meta charset="utf-8">
<title>Ventoras – Gourmet Alfajores</title>
<link rel="stylesheet" href="https://fonts.googleapis.com/css2?family=Berkshire+Swash&display=swap">
<style>
  :root {
    --cream-light: #f7f1e6;
    --cream: #ece2cf;
    --cream-edge: #d9ccb3;
    --wine: #7d1820;
    --wine-dark: #5a0f15;
    --wine-deep: #4a0b10;
    --gold: #c9a55e;
    --name-cream: #f3e6cc;
    --product-light: #eee7db;
    --product-mid: #d9c4a0;
  }
  html, body {
    margin: 0;
    padding: 0;
    width: 849px;
    height: 1200px;
    overflow: hidden;
  }
  .label {
    position: relative;
    width: 849px;
    height: 1200px;
    overflow: hidden;
    background: radial-gradient(ellipse at 50% 45%, var(--cream-light) 0%, var(--cream) 60%, var(--cream-edge) 100%);
    font-family: "Berkshire Swash", cursive;
  }
  .brand-band {
    position: absolute;
    left: 0;
    top: 162px;
    width: 849px;
    height: 50px;
    background: linear-gradient(180deg, var(--wine) 0%, var(--wine-dark) 100%);
    border-top: 3px solid var(--wine-deep);
    border-bottom: 3px solid var(--wine-deep);
  }
  .brand-badge {
    position: absolute;
    left: 170px;
    top: 48px;
    width: 505px;
    height: 290px;
  }
  .brand-name {
    position: absolute;
    left: 170px;
    top: 62px;
    width: 505px;
    height: 290px;
    display: flex;
    align-items: center;
    justify-content: center;
    margin: 0;
    font-weight: 400;
    font-size: 90px;
    color: var(--name-cream);
    letter-spacing: 1px;
  }
  .product-name {
    position: absolute;
    left: 0;
    top: 420px;
    width: 849px;
    margin: 0;
    text-align: center;
    font-weight: 400;
    font-size: 62px;
    color: var(--wine);
  }
  .product-image {
    position: absolute;
    left: 156px;
    top: 594px;
    width: 566px;
    height: 410px;
    border-radius: 24px;
    background: linear-gradient(180deg, var(--product-light) 0%, var(--product-mid) 100%);
  }
  .established {
    position: absolute;
    left: 0;
    top: 1058px;
    width: 849px;
    margin: 0;
    text-align: center;
    font-size: 52px;
    color: var(--wine);
  }
</style>
</head>
<body>
  <main class="label">
    <div class="brand-band"></div>

    <svg class="brand-badge" viewBox="0 0 505 290" aria-hidden="true">
      <defs>
        <radialGradient id="badge-fill" cx="50%" cy="45%" r="60%">
          <stop offset="0%" stop-color="#8e1d26"/>
          <stop offset="100%" stop-color="#560d13"/>
        </radialGradient>
      </defs>
      <ellipse cx="252.5" cy="145" rx="248" ry="140" fill="url(#badge-fill)" stroke="var(--gold)" stroke-width="4"/>
    </svg>
    <h1 class="brand-name">Ventoras</h1>

    <h2 class="product-name">Gourmet Alfajores</h2>

    <div class="product-image" role="img" aria-label="Product photo: an alfajor sandwich cookie dusted with powdered sugar, a bite taken out, caramel filling visible"></div>

    <p class="established">est. 1996</p>
  </main>
</body>
</html>
```